Healthcare IT firm needs classy and unique business care design

We need a business card design that incorporates our new logo design (attached) Prefer a purple based designed. I would really love to see something utilizing the "3D" version of the logo (purple on the reflective wall). I want something a little more than my logo printed along with a person's detailed contact information.
Contact Information for Business Card
Want something polished, professional, and a little unique in the design.
Colors
6b449b
Requirements
Must have
- Please use similar font as the logo design
Nice to have
- Would like to see the 3d version of my logo incorporated into the design.

```html
<!DOCTYPE html>
<html lang="en">
<head>
<meta charset="utf-8">
<title>Brightwell Care Systems – Business Card</title>
<link href="https://fonts.googleapis.com/css2?family=Montserrat:wght@500;600;700&display=swap" rel="stylesheet">
<style>
  :root {
    --backdrop: #2b2b2b;
    --brand-purple: #6b449b;
    --deep-purple: #4a2a78;
    --card-white: #f1f1f1;
    --ink: #2e2e2e;
    --ink-soft: #555555;
    --on-purple: #ffffff;
  }
  * { margin: 0; padding: 0; box-sizing: border-box; }
  html, body {
    width: 1200px;
    height: 1000px;
    overflow: hidden;
    background: var(--backdrop);
    font-family: "Montserrat", Arial, sans-serif;
  }
  .canvas { position: relative; width: 1200px; height: 1000px; }

  .card { position: absolute; }

  .card-front {
    left: 290px; top: 72px;
    width: 651px; height: 390px;
    background: var(--brand-purple);
    display: flex; align-items: center; justify-content: center;
  }
  .front-wordmark {
    color: var(--on-purple);
    font-weight: 600;
    font-size: 40px;
    letter-spacing: -0.5px;
  }

  .card-back {
    left: 290px; top: 556px;
    width: 656px; height: 393px;
    background: var(--card-white);
  }
  .back-wordmark {
    position: absolute;
    left: 45px; top: 52px;
    color: var(--deep-purple);
    font-weight: 600;
    font-size: 31px;
    letter-spacing: -0.5px;
  }
  .holder-name {
    position: absolute;
    left: 45px; top: 211px;
    color: var(--ink);
    font-weight: 700;
    font-size: 19px;
    letter-spacing: 0.3px;
  }
  .holder-role {
    position: absolute;
    left: 45px; top: 235px;
    color: var(--ink-soft);
    font-weight: 600;
    font-size: 13px;
  }
  .name-rule {
    position: absolute;
    left: 45px; top: 259px;
    width: 60px; height: 3px;
    background: var(--deep-purple);
  }
  .contact {
    position: absolute;
    left: 45px; top: 293px;
    color: var(--ink-soft);
    font-weight: 600;
    font-size: 14.5px;
    line-height: 22px;
    letter-spacing: 0.2px;
  }
  .contact .sep {
    color: var(--brand-purple);
    margin: 0 9px;
  }
</style>
</head>
<body>
  <div class="canvas">
    <section class="card card-front">
      <div class="front-wordmark">Brightwell Care Systems</div>
    </section>

    <section class="card card-back">
      <div class="back-wordmark">Brightwell Care Systems</div>
      <div class="holder-name">DANIEL HARTLEY</div>
      <div class="holder-role">Founder &amp; Director</div>
      <div class="name-rule"></div>
      <div class="contact">
        <div>0400 555 218<span class="sep">\</span>daniel@brightwell.example<span class="sep">\</span>www.brightwell.example</div>
        <div>4200 Example Road, 210, Lakeside, VA 20000</div>
      </div>
    </section>
  </div>
</body>
</html>
```